Dental Practice Billboard Design

We are a newer dental practice in need of a simple but appealing billboard for our growing dental practice to attract new patients. The practice is owned by husband and wife dentists and is family friendly in a small town in Kentucky. We try to be very friendly and caring to our patients. Would prefer a blue background for the billboard and our tooth logo to be prominent. We are partial to the Patua One font used in the image below but please feel free to tweak it as you deem necessary. The shape of the uppercase D and lowercase g are why we like that font, so fonts with a similarly shaped “D” and “g” would work as well. Please include our phone number (606) 847-3962. Please see our website Harlowfamilydentistry.com for more info on the practice if needed. Thank you! Looking forward to seeing your creation.
Updates

The dimensions will be 12ft x 24ft (3.6576m x 7.3152m). Apologies for not including this in the original prompt. Thank you all for your submissions.

Industry/Entity Type

Dental

Font styles to use
Other font styles liked:
• Patua One

Colors
0054AA
0677BA
7BADD7
CADEEF
E8F1F8
0094D4
00A9DD
6FCCEA
C7EBF8
E9F6FB
00AB8E
00BBA5
67D7C9
C6EFE9
E9F9F6
59FF00
82FF00
B8FF75
E3FFCB
F4FFEA

Requirements
Must have
• Phone number, website, Logo, Practice name “Harlow Family Dentistry”
Should not have
• A tagline or slogan

```html
<!DOCTYPE html>
<html lang="en">
<head>
<meta charset="UTF-8">
<title>Harlow Family Dentistry Billboard</title>
<link href="https://fonts.googleapis.com/css2?family=Patua+One&family=Montserrat:wght@600;700;800&display=swap" rel="stylesheet">
<style>
  :root {
    --brand-blue: #0457c2;
    --brand-green: #22b24c;
    --ink-dark: #111418;
    --paper: #ffffff;
    --stage: #e9eef4;
    --photo-light: #eef1f5;
    --photo-skin: #d9a184;
    --photo-dark: #4a3328;
  }
  * { margin: 0; padding: 0; box-sizing: border-box; }
  html, body {
    width: 1200px; height: 900px; overflow: hidden;
    background: var(--stage);
  }
  .billboard {
    position: absolute; left: 40px; top: 170px;
    width: 1120px; height: 560px;
    background: var(--brand-blue);
    overflow: hidden;
    font-family: "Montserrat", Arial, sans-serif;
  }
  .brand {
    position: absolute; left: 50px; top: 38px;
    display: flex; align-items: center; gap: 14px;
  }
  .brand-dot {
    width: 44px; height: 44px; border-radius: 50%;
    background: var(--paper);
  }
  .brand-name {
    font-family: "Patua One", Georgia, serif;
    color: var(--paper); font-size: 28px; line-height: 1.1;
  }
  .team-photo {
    position: absolute; left: 0; top: 140px;
    width: 500px; height: 420px;
    background: linear-gradient(180deg, var(--photo-dark) 0%, var(--photo-skin) 28%, var(--photo-light) 58%, var(--paper) 100%);
    border-radius: 120px 120px 0 0;
    z-index: 2;
  }
  .feature {
    position: absolute; left: 530px; top: 90px; width: 560px;
    color: var(--paper);
  }
  .feature-name {
    font-family: "Patua One", Georgia, serif;
    font-size: 76px; line-height: 1.02;
  }
  .feature-name .accent { color: var(--brand-green); display: block; }
  .web {
    margin-top: 24px;
    font-size: 28px; font-weight: 700; color: var(--paper);
  }
  .call-band {
    position: absolute; left: 460px; top: 425px;
    width: 660px; height: 135px;
    background: var(--paper);
    z-index: 1;
    display: flex; align-items: center; gap: 22px;
    padding-left: 90px;
  }
  .call-icon { width: 72px; height: 72px; flex: none; }
  .call-label {
    color: var(--ink-dark); font-weight: 800; font-size: 24px; letter-spacing: 0.5px;
  }
  .call-number {
    color: var(--brand-green); font-weight: 800; font-size: 50px; line-height: 1.05;
  }
</style>
</head>
<body>
  <main class="billboard">
    <div class="brand">
      <span class="brand-dot"></span>
      <div class="brand-name">Harlow<br>Family Dentistry</div>
    </div>

    <div class="team-photo" role="img" aria-label="Photo of the two dentists smiling in white coats"></div>

    <div class="feature">
      <h1 class="feature-name">Harlow<span class="accent">Family Dentistry</span></h1>
      <p class="web">Harlowfamilydentistry.com</p>
    </div>

    <section class="call-band">
      <svg class="call-icon" viewBox="0 0 72 72" aria-hidden="true">
        <path d="M14 20c0-4 4-8 8-8l6 12-5 5c3 7 9 13 16 16l5-5 12 6c0 4-4 8-8 8C28 54 14 38 14 20z" fill="var(--brand-blue)"/>
        <path d="M40 16a18 18 0 0 1 16 16" stroke="var(--brand-blue)" stroke-width="5" fill="none" stroke-linecap="round"/>
        <path d="M40 6a28 28 0 0 1 26 26" stroke="var(--brand-blue)" stroke-width="5" fill="none" stroke-linecap="round"/>
        <path d="M40 26a8 8 0 0 1 6 6" stroke="var(--brand-blue)" stroke-width="5" fill="none" stroke-linecap="round"/>
      </svg>
      <div class="call-text">
        <div class="call-label">CALL US TODAY :</div>
        <div class="call-number">(606) 847-3962</div>
      </div>
    </section>
  </main>
</body>
</html>
```